Business Card Design Project

for a second hand vintage clothing store. shop name is The Velvet Cupboard

Cards to be double sided

The name on the card is Joanna Whitfield

Information to put on card:

The Velvet Cupboard
Joanna Whitfield (no job title)
42/871 Dunmore St, Glenwick, Sydney, NSW, 2009.
Mobile: 0412 905 261
Email: thevelvetcupboard@mailbox.com.au
Web: www.thevelvetcupboard.com.au

Target Market(s)

Women looking at vintage clothing

Industry/Entity Type

Clothing

```html
<!DOCTYPE html>
<html lang="en">
<head>
<meta charset="utf-8">
<title>The Velvet Cupboard — Business Card</title>
<link rel="stylesheet" href="https://fonts.googleapis.com/css2?family=Cormorant+Garamond:wght@600&family=Lato:wght@400&display=swap">
<style>
  :root {
    --plum: #5a2338;
    --plum-soft: #6e3a4b;
    --plum-faint: #7d4c59;
    --cream: #f1dc9c;
    --gold: #c9a233;
    --rose: #e7a6b9;
    --paper: #ffffff;
    --backdrop: #ecebe8;
    --ink-light: #f6eef0;
  }
  * { box-sizing: border-box; margin: 0; padding: 0; }
  html, body { width: 1200px; height: 799px; overflow: hidden; }
  body {
    background: var(--backdrop);
    display: flex;
    align-items: center;
    justify-content: center;
    gap: 60px;
  }
  .card {
    position: relative;
    width: 520px;
    height: 312px;
    overflow: hidden;
    box-shadow: 0 4px 18px rgba(0,0,0,0.18);
  }

  /* Front */
  .card-front { background: var(--plum); }
  .front-ornament {
    position: absolute;
    left: 0; top: 0;
    width: 300px; height: 240px;
    background: radial-gradient(ellipse at 35% 30%, var(--plum-faint) 0%, rgba(110,58,75,0.6) 40%, rgba(90,35,56,0) 75%);
  }
  .front-brand {
    position: absolute;
    left: 0; right: 0; top: 110px;
    display: flex;
    align-items: center;
    justify-content: center;
    gap: 14px;
  }
  .front-brand .mark {
    width: 14px; height: 14px;
    border-radius: 50%;
    background: var(--cream);
  }
  .front-brand .name {
    font-family: "Cormorant Garamond", serif;
    font-weight: 600;
    font-size: 46px;
    color: var(--cream);
    letter-spacing: 0.5px;
  }

  /* Back */
  .card-back { background: var(--paper); }
  .back-brand {
    position: absolute;
    left: 26px; top: 36px;
    font-family: "Cormorant Garamond", serif;
    font-weight: 600;
    font-size: 22px;
    color: var(--gold);
  }
  .back-flourish-top {
    position: absolute;
    right: 40px; top: 14px;
    width: 130px; height: 34px;
    background: linear-gradient(90deg, rgba(231,166,185,0) 0%, var(--rose) 50%, rgba(231,166,185,0) 100%);
    opacity: 0.55;
    border-radius: 20px;
  }
  .back-name-row {
    position: absolute;
    left: 26px; right: 26px; top: 76px;
    display: flex;
    align-items: center;
    gap: 14px;
  }
  .flourish-small {
    width: 60px; height: 14px;
    background: linear-gradient(90deg, rgba(231,166,185,0.2), var(--rose));
    border-radius: 10px;
  }
  .flourish-small.right { background: linear-gradient(90deg, var(--rose), rgba(231,166,185,0.2)); }
  .person-name {
    font-family: "Cormorant Garamond", serif;
    font-weight: 600;
    font-size: 30px;
    color: var(--plum);
    letter-spacing: 1px;
  }
  .contact-band {
    position: absolute;
    left: 0; right: 0; top: 124px;
    height: 140px;
    background: var(--plum);
    padding: 16px 26px;
    font-family: "Lato", sans-serif;
    font-style: normal;
    font-size: 13px;
    line-height: 1.6;
    color: var(--ink-light);
  }
  .contact-band .label { color: var(--cream); }
</style>
</head>
<body>

  <section class="card card-front" aria-label="Card front">
    <div class="front-ornament" role="img" aria-label="Faint floral swirl ornament in muted plum"></div>
    <div class="front-brand">
      <span class="mark"></span>
      <span class="name">The Velvet Cupboard</span>
    </div>
  </section>

  <section class="card card-back" aria-label="Card back">
    <div class="back-brand">The Velvet Cupboard</div>
    <div class="back-flourish-top" role="img" aria-label="Pink calligraphic flourish ornament"></div>
    <div class="back-name-row">
      <div class="flourish-small" role="img" aria-label="Small pink leaf flourish"></div>
      <div class="person-name">Joanna Whitfield</div>
      <div class="flourish-small right" role="img" aria-label="Small pink leaf flourish"></div>
    </div>
    <address class="contact-band">
      42/871 Dunmore St, Glenwick<br>
      Sydney, NSW, 2009<br>
      <span class="label">M</span> 0412 905 261<br>
      <span class="label">E</span> thevelvetcupboard@mailbox.com.au<br>
      <span class="label">W</span> www.thevelvetcupboard.com.au
    </address>
  </section>

</body>
</html>
```